A pop-banner and Image for a magazine

Pop-up 100cm x 200cm:
Harbourvale Junior Ensembles
Circle of Sound Scheme
Give the Gift of Music

Supporter – €100
Contributes to rehearsal space, music and essential administration.

Champion – €250
Funds coaching, instrument supports and performance opportunities.

Patron – €450
Sponsors a full membership for a young musician where cost is a barrier.

All Circle of Sound Members are acknowledged in concert programmes.
Graphic for Magazine - A4:
HJE - Circle of Sound Scheme
Give the gift of music this year

Circle of Sound – Supporter (€100)
A Supporter helps with the core running costs of HJE such as rehearsal space, music purchase and essential administration. This contribution strengthens the day-to-day foundation that allows over 300 young musicians to learn and perform. Supporters are acknowledged in concert programmes.
Circle of Sound – Champion (€250)
Champions provide deeper backing that directly enhances the musical experience for our ensembles. This level helps fund sectional coaching, instrument supports and performance opportunities. Champions are acknowledged in our programmes and receive an annual note of thanks outlining the impact of their contribution.
Circle of Sound – Patron (€450)
Our Patron tier directly supports social inclusion and participation within HJE. A contribution at this level helps fund a full membership place for a young musician who would otherwise be unable to take part due to financial barriers.
By becoming a Patron, you ensure that every talented player has the chance to rehearse, perform and grow within the orchestra. Patrons are acknowledged in concert programmes and receive priority notice of major events, along with a yearly update on the positive impact of their support.

Industry/Entity Type

Music - please refer to the website for logo and colours

Requirements
Must have
• https://www.hje-example.ie/

```html
<!DOCTYPE html>
<html lang="en">
<head>
<meta charset="utf-8">
<title>Circle of Sound Scheme</title>
<link href="https://fonts.googleapis.com/css2?family=Big+Shoulders+Display:wght@300&family=Poppins:wght@300;400;500;600&display=swap" rel="stylesheet">
<style>
  :root {
    --pink: #e91e5f;
    --purple: #6a3d9a;
    --badge-purple: #7a52a8;
    --ink: #231f20;
    --body: #3a3a3a;
    --rule: #cfcfcf;
    --paper: #ffffff;
  }
  * { margin: 0; padding: 0; box-sizing: border-box; }
  html, body { width: 924px; height: 1200px; overflow: hidden; background: var(--paper); }
  body { font-family: "Poppins", sans-serif; color: var(--ink); }
  .sheet { position: relative; width: 924px; height: 1200px; overflow: hidden; }

  .brand { position: absolute; left: 0; right: 0; top: 78px; display: flex; justify-content: center; align-items: center; gap: 16px; }
  .brand-mark { width: 62px; height: 62px; background: var(--purple); }
  .brand-name { font-weight: 600; font-size: 28px; line-height: 1.05; color: var(--ink); }
  .brand-sub { font-weight: 500; font-size: 13px; color: var(--pink); margin-top: 6px; }

  .decor { position: absolute; }
  .decor-note-top { right: 0; top: 205px; width: 90px; height: 240px; border-radius: 45px 0 0 45px;
    background: linear-gradient(160deg, #f9b233 0%, #f47a3a 45%, #e91e78 100%); }
  .decor-dot { right: 20px; top: 186px; width: 14px; height: 14px; border-radius: 50%; background: #f2a93b; }
  .decor-clef { left: 46px; top: 580px; width: 64px; height: 96px; border-radius: 32px;
    background: linear-gradient(150deg, #b25ed6, #5a2a8e); }

  .title-top { position: absolute; top: 232px; left: 0; right: 0; text-align: center; font-weight: 500; font-size: 44px; letter-spacing: -0.5px; }
  .title-main { position: absolute; top: 296px; left: 0; right: 0; text-align: center; font-family: "Big Shoulders Display", sans-serif; font-weight: 300; font-size: 128px; line-height: 1; letter-spacing: 2px; }
  .title-main .a { color: var(--pink); }
  .title-main .b { color: var(--purple); }

  .photo { position: absolute; width: 201px; height: 169px; }
  .photo-violin { left: 68px; top: 449px; background: radial-gradient(circle at 55% 40%, #6b3a22, #2a140c 75%); }
  .photo-duo { left: 652px; top: 690px; background: radial-gradient(circle at 70% 60%, #c2692a, #1d120d 70%); }
  .photo-hall { left: 68px; top: 938px; background: linear-gradient(180deg, #4a3a2e 0%, #a4713f 45%, #3a2417 100%); }

  .tier-head { position: absolute; display: flex; align-items: center; gap: 26px; }
  .tier-title { font-weight: 500; font-size: 22px; letter-spacing: -0.4px; color: var(--ink); white-space: nowrap; }
  .badge { width: 197px; height: 44px; display: flex; align-items: center; justify-content: center; color: #fff; font-weight: 500; font-size: 19px; }
  .badge-pink { background: var(--pink); }
  .badge-purple { background: var(--badge-purple); }

  .tier-text { position: absolute; font-weight: 300; font-size: 16px; line-height: 21.5px; color: var(--body); letter-spacing: -0.3px; }

  .rule { position: absolute; left: 68px; width: 783px; height: 1px; background: var(--rule); }
</style>
</head>
<body>
<main class="sheet">
  <header class="brand">
    <div class="brand-mark"></div>
    <div>
      <div class="brand-name">Harbourvale Junior<br>Ensembles</div>
      <div class="brand-sub">Ceolfhoirne Óga Chuan Gleanna</div>
    </div>
  </header>

  <div class="decor decor-dot"></div>
  <div class="decor decor-note-top" role="img" aria-label="Glossy orange and pink music note"></div>

  <h1>
    <span class="title-top">CIRCLE OF</span>
    <span class="title-main"><span class="a">SOUND</span> <span class="b">SCHEME</span></span>
  </h1>

  <section>
    <div class="photo photo-violin" role="img" aria-label="Violinist performing in a concert hall"></div>
    <div class="decor decor-clef" role="img" aria-label="Glossy purple treble clef"></div>
    <div class="tier-head" style="left:331px; top:449px;">
      <h2 class="tier-title">CIRCLE OF SOUND</h2>
      <span class="badge badge-pink" style="margin-left:20px;">Supporter (€100)</span>
    </div>
    <p class="tier-text" style="left:333px; top:507px; width:550px;">A Supporter helps cover HJE’s essential running costs, including rehearsal space, music purchases and core administration. This contribution strengthens the foundation that enables over 300 young musicians to learn, grow and perform. Supporters are acknowledged in our concert programmes.</p>
  </section>

  <div class="rule" style="top:654px;"></div>

  <section>
    <div class="tier-head" style="left:66px; top:689px;">
      <h2 class="tier-title">CIRCLE OF SOUND</h2>
      <span class="badge badge-purple" style="margin-left:90px;">Champion (€250)</span>
    </div>
    <p class="tier-text" style="left:68px; top:748px; width:555px;">Champions provide enhanced support that directly improves the musical experience for our ensembles. This level contributes to sectional coaching, instrument supports and performance opportunities. Champions are acknowledged in our programmes and receive an annual note of thanks detailing the impact of their contribution.</p>
    <div class="photo photo-duo" role="img" aria-label="Trumpet and double bass players on a dark stage"></div>
  </section>

  <div class="rule" style="top:902px;"></div>

  <section>
    <div class="photo photo-hall" role="img" aria-label="Orchestra performing in a large concert hall"></div>
    <div class="tier-head" style="left:331px; top:938px;">
      <h2 class="tier-title">CIRCLE OF SOUND</h2>
      <span class="badge badge-pink" style="margin-left:20px;">Patron (€450)</span>
    </div>
    <p class="tier-text" style="left:333px; top:996px; width:550px;">Our Patron tier plays a vital role in social inclusion and accessibility. A contribution at this level funds a full membership for a young musician who would otherwise be unable to participate due to financial barriers.<br>Patrons are acknowledged in concert programmes, receive priority notice of major events, and are provided with a yearly update on the positive difference their support makes.</p>
  </section>
</main>
</body>
</html>
```